Small but growing painting company. Have built up a steady client base. Want to start having a more professional look. Want to start with changing my business cards, and also getting new logo and tee shirts.

Target Market(s)

Home owners, property management companies, all ages 30-70

Industry/Entity Type

Painting And Decorating

Contact Information for Business Card

Bright Ridge Painting LLC Mark Delvecchi 630-584-3907 interior, exterior, vaulted ceiling, drywall repair, pressure washing, kitchen cabinets, epoxy, garage floors,

Font styles to use
Sans Serif
Other font styles liked:
• Harrington

Colors
0355a3
ffffff
ec1f27
000000
3176b5
0493ce
474747
b7b7b7

Requirements
Must have
• Creative, something that doesn’t look like every other painting card.
Nice to have
• I would like something with an arrow or something going to a point

```html
<!DOCTYPE html>
<html lang="en">
<head>
<meta charset="utf-8">
<title>Bright Ridge Painting LLC – Business Card</title>
<link rel="stylesheet" href="https://fonts.googleapis.com/css2?family=Oswald:wght@400;500&family=Lato:wght@400&display=swap">
<style>
  :root {
    --backdrop: #8c8c8c;
    --card-light: #ffffff;
    --card-dark: #3a3939;
    --brand-red: #ec1f27;
    --ink: #2b2b2b;
    --rule: #9a9a9a;
    --light-text: #ffffff;
  }
  html, body { margin: 0; padding: 0; overflow: hidden; }
  body {
    width: 1200px; height: 1200px;
    background: var(--backdrop);
    position: relative;
    font-family: "Lato", sans-serif;
  }
  .card {
    position: absolute;
    top: 310px;
    height: 594px;
    box-shadow: 2px 3px 5px rgba(0,0,0,0.45);
    text-align: center;
  }
  .card--front { left: 234px; width: 364px; background: var(--card-light); }
  .card--back  { left: 627px; width: 370px; background: var(--card-dark); }

  .brand-mark {
    position: absolute; left: 50%; transform: translateX(-50%);
    border-radius: 50%; background: var(--brand-red);
  }
  .card--front .brand-mark { top: 100px; width: 130px; height: 130px; }
  .card--back .brand-mark  { top: 170px; width: 200px; height: 200px; }

  .brand-name {
    position: absolute; left: 0; right: 0;
    font-family: "Oswald", sans-serif; font-weight: 500;
    text-transform: uppercase; letter-spacing: 0.2px;
  }
  .card--front .brand-name { top: 262px; font-size: 28px; color: var(--ink); }
  .card--back .brand-name { top: 392px; font-size: 20px; color: var(--light-text); }

  .person-name {
    position: absolute; top: 402px; left: 0; right: 0;
    font-family: "Oswald", sans-serif; font-weight: 400;
    font-size: 27px; color: var(--brand-red); text-transform: uppercase;
  }
  .contact-divider {
    position: absolute; top: 454px; left: 87px; width: 190px; height: 24px;
    display: flex; align-items: center; justify-content: center; gap: 4px;
  }
  .contact-divider::before, .contact-divider::after {
    content: ""; flex: 1; height: 1px; background: var(--rule);
  }
  .contact-divider svg { display: block; }
  .contact-list {
    position: absolute; top: 488px; left: 0; right: 0;
    margin: 0; padding: 0; list-style: none;
    font-size: 17px; line-height: 22px; color: var(--ink);
  }
  .services {
    position: absolute; top: 488px; left: 0; right: 0;
    margin: 0; font-size: 17.5px; line-height: 22px; color: var(--light-text);
  }
  .services .dot { color: var(--brand-red); font-size: 12px; vertical-align: 2px; padding: 0 3px; }
</style>
</head>
<body>
  <section class="card card--front">
    <div class="brand-mark" aria-hidden="true"></div>
    <div class="brand-name">Bright Ridge Painting LLC</div>
    <div class="person-name">Mark Delvecchi</div>
    <div class="contact-divider">
      <svg width="80" height="24" viewBox="0 0 80 24" aria-hidden="true">
        <circle cx="12" cy="12" r="11" fill="#ec1f27"/>
        <path d="M7 9 q5 -4 10 0 l-2 2 -1.5 -1 h-3 l-1.5 1z M9 12 h6 l1 4 h-8z" fill="#fff"/>
        <circle cx="40" cy="12" r="11" fill="#ec1f27"/>
        <rect x="34" y="8" width="12" height="8" fill="none" stroke="#fff" stroke-width="1.4"/>
        <path d="M34 8 l6 5 6 -5" fill="none" stroke="#fff" stroke-width="1.4"/>
        <circle cx="68" cy="12" r="11" fill="#ec1f27"/>
        <circle cx="68" cy="12" r="6" fill="none" stroke="#fff" stroke-width="1.4"/>
        <path d="M62 12 h12 M68 6 v12" stroke="#fff" stroke-width="1.2"/>
      </svg>
    </div>
    <ul class="contact-list">
      <li>630-584-3907</li>
      <li>info@webname.com</li>
      <li>www.websitename.com</li>
    </ul>
  </section>

  <section class="card card--back">
    <div class="brand-mark" aria-hidden="true"></div>
    <div class="brand-name">Bright Ridge Painting LLC</div>
    <p class="services">
      Interior<span class="dot">●</span>Exterior<span class="dot">●</span>Vaulted Ceiling<br>
      Drywall Repair<span class="dot">●</span> Pressure Washing<br>
      Kitchen Cabinets<span class="dot">●</span>Epoxy<span class="dot">●</span>Garage Floors.
    </p>
  </section>
</body>
</html>
```